Copperleaf Motorized Shade Business Card

Hello, we've had our logo made. Now we are looking for a clean and cool looking business card. One side can just be the logo with any design elements that might look good with it. The other side will be Name, Phone Number and Email. There will not be an address on the card.

```html
<!DOCTYPE html>
<html lang="en">
<head>
<meta charset="utf-8">
<title>Copperleaf Motorized Shade Business Card</title>
<link rel="stylesheet" href="https://fonts.googleapis.com/css2?family=Lato:wght@400;700;900&display=swap">
<style>
  :root {
    --stage: #2a2a2a;
    --navy: #0b3f86;
    --navy-deep: #083370;
    --sky: #1e9be0;
    --sun: #f7b818;
    --paper: #f7f7f5;
    --ink: #5a5a5a;
  }
  * { box-sizing: border-box; margin: 0; padding: 0; }
  html, body {
    width: 1200px; height: 896px; overflow: hidden;
    background: var(--stage);
    font-family: "Lato", sans-serif;
  }
  .stage {
    position: relative; width: 1200px; height: 896px;
    display: flex; align-items: center; justify-content: center; gap: 48px;
  }
  .card {
    position: relative; width: 525px; height: 300px; flex: none;
    border-radius: 3px; overflow: hidden;
    box-shadow: 0 14px 30px rgba(0,0,0,.5);
  }
  /* Front: logo side */
  .card-front { background: var(--navy); }
  .front-texture {
    position: absolute; inset: 0;
    background: linear-gradient(135deg, #0d4790 0%, var(--navy) 50%, var(--navy-deep) 100%);
  }
  .front-wordmark {
    position: absolute; inset: 0; padding: 0 48px;
    display: flex; align-items: center; justify-content: center; gap: 16px;
  }
  .mark-square { width: 22px; height: 22px; background: #ffffff; flex: none; }
  .front-wordmark .brand-name {
    color: #ffffff; font-weight: 900; font-size: 34px; line-height: 1.1;
    text-transform: uppercase; letter-spacing: 1px; white-space: nowrap;
  }
  /* Back: contact side */
  .card-back { background: var(--paper); }
  .back-logo {
    position: absolute; left: 40px; top: 110px; width: 200px;
    display: flex; align-items: flex-start; gap: 10px;
  }
  .back-logo .mark-square { width: 16px; height: 16px; background: var(--navy); margin-top: 4px; }
  .back-logo .brand-name {
    color: var(--navy); font-weight: 900; font-size: 22px; line-height: 1.1;
    text-transform: uppercase;
  }
  .divider {
    position: absolute; left: 258px; top: 70px; width: 2px; height: 140px;
    background: var(--sun);
  }
  .contact { position: absolute; left: 282px; top: 72px; }
  .person-name {
    color: var(--navy); font-weight: 900; font-size: 21px; text-transform: uppercase;
  }
  .person-role { color: var(--ink); font-size: 15px; margin-top: 2px; }
  .contact-list { list-style: none; margin-top: 18px; }
  .contact-list li {
    display: flex; align-items: center; gap: 8px;
    color: var(--ink); font-size: 15px; line-height: 1.55; white-space: nowrap;
  }
  .contact-list svg { width: 12px; height: 12px; fill: var(--sky); flex: none; }
  .edge-band {
    position: absolute; left: 0; right: 0; bottom: 0; height: 12px;
    display: flex;
  }
  .edge-band .band-light { flex: 3; background: var(--sky); }
  .edge-band .band-dark { flex: 1; background: var(--navy); }
</style>
</head>
<body>
<main class="stage">
  <section class="card card-front" aria-label="Card front">
    <div class="front-texture" role="img" aria-label="Repeating pattern of shade and window motifs on navy"></div>
    <div class="front-wordmark">
      <span class="mark-square"></span>
      <span class="brand-name">Copperleaf<br>Motorized Shades</span>
    </div>
  </section>

  <section class="card card-back" aria-label="Card back">
    <div class="back-logo">
      <span class="mark-square"></span>
      <span class="brand-name">Copperleaf<br>Motorized<br>Shades</span>
    </div>
    <div class="divider"></div>
    <div class="contact">
      <p class="person-name">Dana Whitlow</p>
      <p class="person-role">Founder &amp; CEO</p>
      <ul class="contact-list">
        <li><svg viewBox="0 0 24 24"><path d="M6.6 10.8a15 15 0 0 0 6.6 6.6l2.2-2.2a1 1 0 0 1 1-.25 11.4 11.4 0 0 0 3.6.57 1 1 0 0 1 1 1V20a1 1 0 0 1-1 1A17 17 0 0 1 3 4a1 1 0 0 1 1-1h3.5a1 1 0 0 1 1 1c0 1.25.2 2.45.57 3.57a1 1 0 0 1-.25 1z"/></svg>555-014-2290</li>
        <li><svg viewBox="0 0 24 24"><path d="M2 5h20v14H2z M2 5l10 8 10-8" /></svg>info@copperleafshade.com</li>
        <li><svg viewBox="0 0 24 24"><circle cx="12" cy="12" r="10"/></svg>www.copperleafshade.com</li>
      </ul>
    </div>
    <div class="edge-band"><span class="band-light"></span><span class="band-dark"></span></div>
  </section>
</main>
</body>
</html>
```